Business card design needed

would like the title calloway estate works to itself be a logo which would also be suitable to use on my van signwriting so needs to be bold and stand out (easily read from a distance)
Target Market(s)
real estate agents, property owners/investors,insurance assessors,
Industry/Entity Type
Business
Contact Information for Business Card
calloway estate works
for all your property maintenance and repair needs
-domestic and commercial -rental properties
-insurance repairs -project managment
fully insured/white card
experieced and reliable
ph. ned calloway 0418526093 email nedster4731@webhollow.net.au
on reverse side of card i would like a list of sevices available
plaster repairs
painting
welding reairs and fabrication
concreting
fencing
minor renovations
pressure cleaning
graffitti removal
rubbish removal
fire restorations
floods
and more no job too big or small
Logo Text
Logo styles of interest
Wordmark Logo

```html
<!DOCTYPE html>
<html lang="en">
<head>
<meta charset="utf-8">
<title>Calloway Estate Works – Business Card</title>
<link href="https://fonts.googleapis.com/css2?family=Michroma&display=swap" rel="stylesheet">
<style>
  :root {
    --backdrop: #2b2b2b;
    --card-white: #f6f6f6;
    --deep-red: #9a0000;
    --band-red: #d40000;
    --band-orange: #f0a030;
    --mark-red: #e41a1a;
    --ink-dark: #1e1e1e;
    --ink-grey: #555555;
    --ink-soft: #6a6a6a;
  }
  * { margin: 0; padding: 0; box-sizing: border-box; }
  html, body {
    width: 1200px;
    height: 1000px;
    overflow: hidden;
    background: var(--backdrop);
    font-family: "Michroma", sans-serif;
  }
  .card {
    position: absolute;
    left: 197px;
    width: 805px;
    height: 460px;
    background: var(--card-white);
    overflow: hidden;
    box-shadow: 0 8px 24px rgba(0,0,0,0.5);
  }
  .card-back { top: 25px; }
  .card-front { top: 515px; }
  .card-art { position: absolute; inset: 0; }
  .text { position: absolute; text-transform: uppercase; }

  /* back side */
  .services { right: 40px; top: 40px; text-align: right; color: var(--ink-soft); }
  .services-title { font-size: 19px; letter-spacing: 2px; margin-bottom: 8px; color: var(--ink-grey); }
  .services-list { list-style: none; font-size: 12.5px; line-height: 23px; letter-spacing: 1px; }
  .closing { right: 40px; bottom: 36px; text-align: right; color: var(--ink-dark); font-size: 15px; line-height: 26px; letter-spacing: 1.5px; }

  /* front side */
  .intro { left: 52px; top: 74px; color: var(--ink-dark); }
  .company { font-size: 19px; letter-spacing: 1.5px; margin-bottom: 6px; }
  .offer { list-style: none; font-size: 9.5px; line-height: 15px; letter-spacing: 1px; }
  .contact { left: 52px; bottom: 34px; }
  .person { font-size: 40px; letter-spacing: 4px; color: var(--ink-dark); margin-bottom: 8px; }
  .phone { font-size: 22px; letter-spacing: 3px; color: var(--ink-grey); margin-bottom: 4px; }
  .email { font-size: 17px; letter-spacing: 1.5px; color: var(--ink-grey); }
</style>
</head>
<body>

<section class="card card-back" aria-label="Card reverse: services">
  <svg class="card-art" viewBox="0 0 805 460" aria-hidden="false">
    <rect width="805" height="460" fill="var(--deep-red)"/>
    <circle cx="760" cy="200" r="650" fill="var(--band-red)"/>
    <circle cx="760" cy="200" r="610" fill="var(--band-orange)"/>
    <circle cx="760" cy="200" r="565" fill="var(--band-red)"/>
    <circle cx="760" cy="200" r="530" fill="var(--card-white)"/>
    <g class="wordmark" fill="var(--mark-red)" font-family="Michroma, sans-serif">
      <text transform="translate(62 440) rotate(-90)" font-size="40" letter-spacing="4">CALLOWAY</text>
      <text transform="translate(98 440) rotate(-90)" font-size="18" letter-spacing="3">ESTATE WORKS</text>
    </g>
  </svg>
  <div class="text services">
    <h2 class="services-title">Services Available</h2>
    <ul class="services-list">
      <li>Plaster repairs,</li>
      <li>Painting, welding,</li>
      <li>Reairs and fabrication,</li>
      <li>Concreting, fencing,</li>
      <li>Minor renovations,</li>
      <li>Pressure cleaning,</li>
      <li>Graffitti removal,</li>
      <li>Rubbish removal,</li>
      <li>Fire restorations,</li>
      <li>Floods.</li>
    </ul>
  </div>
  <p class="text closing">And more<br>No job too big or small</p>
</section>

<section class="card card-front" aria-label="Card front: contact details">
  <svg class="card-art" viewBox="0 0 805 460">
    <rect width="805" height="460" fill="var(--deep-red)"/>
    <circle cx="120" cy="210" r="700" fill="var(--band-red)"/>
    <circle cx="120" cy="210" r="660" fill="var(--band-orange)"/>
    <circle cx="120" cy="210" r="615" fill="var(--band-red)"/>
    <circle cx="120" cy="210" r="580" fill="var(--card-white)"/>
  </svg>
  <div class="text intro">
    <h1 class="company">Calloway Estate Works</h1>
    <ul class="offer">
      <li>For all your property maintenance and repair needs</li>
      <li>-Domestic and commercial</li>
      <li>-Rental properties</li>
      <li>-Insurance repairs</li>
      <li>-Project managment fully insured/white card</li>
      <li>-Experienced and reliable</li>
    </ul>
  </div>
  <div class="text contact">
    <p class="person">Ned Calloway</p>
    <p class="phone">0418526093</p>
    <p class="email">nedster4731@webhollow.net.au</p>
  </div>
</section>

</body>
</html>
```